Vesprine Oakville Cabernet Sauvignon-Wine label design

We need a package design for an up market wine brand named, Vesprine. It will be a Cabernet Sauvignon from the Oakville AVA of Napa Valley. We are looking for a stylish modern label that will stand out on a retail shelf. We want the label to be attention grabbing and stylish while presenting an up market luxury brand.

Sick

Requirements
Must have
• Must have the words(in order of importance)
-Vesprine
-Cabernet Sauvignon
-Oakville
-Napa Valley
-2018

Must be designed for a traditional "Bordeaux" style bottle (Bottle specs in uploaded files)
Should not have
• Any images of grapes, vineyards, wine glasses or bottles

```html
<!DOCTYPE html>
<html lang="en">
<head>
<meta charset="utf-8">
<title>Vesprine Cabernet Sauvignon – Label</title>
<link rel="stylesheet" href="https://fonts.googleapis.com/css2?family=Exo+2:wght@500&family=Josefin+Sans:wght@400&family=Cormorant+SC:wght@500&display=swap">
<style>
  :root {
    --backdrop: #3c3c3c;
    --label-black: #000000;
    --texture-grey: #161616;
    --gold: #f2ac3a;
    --white: #ffffff;
    --art-blue: #3fb6d8;
    --art-orange: #f47b20;
  }
  html, body {
    margin: 0;
    padding: 0;
    width: 1200px;
    height: 1200px;
    overflow: hidden;
    background: var(--backdrop);
  }
  .label {
    position: absolute;
    left: 154px;
    top: 51px;
    width: 892px;
    height: 1098px;
    background: var(--label-black);
    overflow: hidden;
  }
  .label__texture {
    position: absolute;
    left: 0;
    top: 0;
    width: 892px;
    height: 700px;
    background: radial-gradient(ellipse 60% 55% at 50% 45%, var(--texture-grey) 0%, var(--label-black) 100%);
  }
  .label__emblem {
    position: absolute;
    left: 247px;
    top: 208px;
    width: 410px;
    height: 410px;
  }
  .label__brand {
    position: absolute;
    top: 690px;
    left: 0;
    width: 100%;
    text-align: center;
    font-family: "Exo 2", sans-serif;
    font-weight: 500;
    font-size: 88px;
    line-height: 88px;
    letter-spacing: 0;
    color: var(--white);
    margin: 0;
  }
  .label__varietal {
    position: absolute;
    top: 873px;
    left: 0;
    width: 100%;
    text-align: center;
    font-family: "Josefin Sans", sans-serif;
    font-size: 25px;
    line-height: 30px;
    letter-spacing: 9px;
    text-indent: 9px;
    color: var(--gold);
    margin: 0;
  }
  .label__origin {
    position: absolute;
    top: 910px;
    left: 0;
    width: 100%;
    text-align: center;
    font-family: "Cormorant SC", serif;
    font-weight: 500;
    font-size: 23px;
    line-height: 26px;
    color: var(--white);
    margin: 0;
  }
  .label__vintage {
    position: absolute;
    top: 933px;
    left: 0;
    width: 100%;
    display: flex;
    justify-content: center;
    align-items: center;
    gap: 17px;
    font-family: "Cormorant SC", serif;
    font-weight: 500;
    font-size: 22px;
    line-height: 26px;
    color: var(--white);
  }
  .label__rule {
    width: 73px;
    height: 2px;
    background: var(--white);
  }
</style>
</head>
<body>
  <main class="label">
    <div class="label__texture" role="img" aria-label="Faint dark-grey decorative pattern behind the emblem"></div>

    <svg class="label__emblem" viewBox="0 0 410 410" role="img" aria-label="Circular gold-framed illustration of a stag's head with antlers, a small bird perched on top, scattered coloured dots and a striped gold shading">
      <defs>
        <radialGradient id="emblem-fill" cx="40%" cy="40%" r="65%">
          <stop offset="0%" stop-color="var(--art-blue)" stop-opacity="0.35"/>
          <stop offset="45%" stop-color="var(--gold)" stop-opacity="0.35"/>
          <stop offset="100%" stop-color="var(--art-orange)" stop-opacity="0.15"/>
        </radialGradient>
      </defs>
      <circle cx="205" cy="205" r="199" fill="url(#emblem-fill)" stroke="var(--gold)" stroke-width="7"/>
    </svg>

    <h1 class="label__brand">VESPRINE</h1>
    <p class="label__varietal">CABERNET SAUVIGNON</p>
    <p class="label__origin">Oakville - Napa Valley</p>
    <div class="label__vintage">
      <span class="label__rule"></span>
      <span>2018</span>
      <span class="label__rule"></span>
    </div>
  </main>
</body>
</html>
```